Gale Sentry - WEBSITE Contest - 4-5 pages coding - Strong, simple clean WORDPRESS

Hello,
The inspiriation website is www.brixhalo.com
Please look at this site because I want to copy that.
I have changed the order a little bit so please look at my order of the site elements.
I will supply text, please just use lorem ipsum for now.
PLEASE LOOK AT THE BRIX HALO WEBSITE AND MAKE A COPY OF THAT.
PPlease look at that site and see the different features it has and make that.
We will need this main page and then:
-About Us page
-Contact Us page
-Request a quote page / fillable form
-1 product/service page
Thank you,
Trevor
/////////////////////////////
Website design for Gale Sentry.
Please design with simple, easy to read fonts. Customers are older and need strong, bold easy to read.
galesentry-demo.com
Tel (555) 318-4072
trevor@galesentry-demo.com
The problem is that all roofing vents leak. We have a product that goes into the vent that stops the roof from leaking.
Your beautiful Florida home is unprotected!
All roof vents leak!
Winds over 30 MPH push rainwater INTO your home through the rooftop vents! The result is water damage that can cost thousands of dollars to repair and remediate!
The GALE SENTRY is a powerful roof vent protection system, engineered to block wind driven rains from entering your home's roof vents.
The Gale Sentry is made to withstand extreme conditions. Featuring IMPACT hurricane screening and powerful steel construction.
Professional installation is permanent and concealed and is accomplished via the roof top.
Get protected for all the storms ahead! Get the Gale Sentry!
www.galesentry-demo.com
Call Now: 555 318-4072
Updates
Hello to all designers - please add a "SERVICE AREA MAP" widget to the designs. Thank you.
Target Market(s)
The target customer is a affluent, older couple 50-60 years old. Homeowner. middle class to upper class adults / ages 50-60 years old (older but not VERY old)
Industry/Entity Type
roofing and construction
Coding
Coded - Design and coding required
Number of Pages Required
4 page
Colors
Designer to choose colors to be used in the design.
Requirements
Must have
- Great landing page, about us page, product page, contact us page, request quote form / Strong, simple clean
Nice to have
- feelings: professional / strong / reliable / safety / shelter / security / future stability/ calm / security
Should not have
- stress / fear feeling - this product will remove fear and stress of damages from storms

```html
<!DOCTYPE html>
<html lang="en">
<head>
<meta charset="utf-8">
<title>Gale Sentry – Roof Vent Protection</title>
<link rel="stylesheet" href="https://fonts.googleapis.com/css2?family=Poppins:wght@300;400;500;600;700&family=Playfair+Display:ital,wght@1,600&display=swap">
<style>
:root{
  --blue:#1f6fb5;
  --blue-dark:#17538c;
  --blue-band:#1a5d9c;
  --ink:#1e2a36;
  --muted:#7a8591;
  --light:#f4f5f7;
  --white:#ffffff;
  --night:#0d1014;
  --shade:rgba(12,16,22,.72);
}
*{box-sizing:border-box;margin:0;padding:0}
html,body{width:1200px;height:4960px;overflow:hidden}
body{font-family:"Poppins",Arial,sans-serif;color:var(--ink);background:var(--white);position:relative}
.accent{font-family:"Playfair Display",Georgia,serif;font-style:italic;color:var(--blue);font-weight:600}
.photo{position:absolute;inset:0}
.shade{position:absolute;inset:0;background:var(--shade)}
section,.site-footer{position:absolute;left:0;width:1200px;overflow:hidden}
.inner{position:relative;z-index:1;width:1200px}
.btn-row{display:flex;justify-content:center;gap:40px}
.btn{display:inline-flex;align-items:center;justify-content:center;gap:8px;height:46px;padding:0 30px;background:var(--blue-dark);color:var(--white);font-size:13px;font-weight:500;border:1px solid rgba(255,255,255,.35);text-decoration:none}
.btn svg{width:12px;height:12px}
.eyebrow{font-size:11px;letter-spacing:4px;text-transform:uppercase;color:rgba(255,255,255,.75);text-align:center}
.lede{font-size:13px;line-height:1.75;text-align:center;width:520px;margin:0 auto}
.divider{width:50px;height:3px;background:var(--blue);margin:18px auto}

/* header & hero */
.hero{top:0;height:552px;color:var(--white)}
.hero .photo{background:linear-gradient(160deg,#4c5258 0%,#2c3136 45%,#5e6469 100%)}
.hero .shade{background:rgba(15,20,26,.55)}
.site-header{position:absolute;z-index:2;top:0;left:0;width:1200px;height:64px;display:flex;align-items:center;padding:0 36px}
.brand{display:flex;align-items:center;gap:12px;font-weight:600;font-size:17px;letter-spacing:1px}
.brand-dot{width:34px;height:34px;border-radius:50%;border:2px solid var(--white)}
.main-nav{margin-left:auto;display:flex;gap:28px;font-size:13px;align-items:center}
.main-nav a{color:var(--white);text-decoration:none}
.nav-phone{display:flex;align-items:center;gap:6px;font-weight:600;font-size:16px}
.nav-phone svg{width:15px;height:15px}
.hero-copy{position:absolute;z-index:1;top:160px;left:0;width:1200px;text-align:center}
.hero-kicker{font-size:20px;letter-spacing:6px;font-weight:300}
.hero-title{font-size:42px;font-weight:700;line-height:1.2;margin:14px 0 42px}

/* approved grid */
.approved{top:552px;height:800px;background:var(--white)}
.section-title{font-size:24px;font-weight:600;text-align:center}
.approved .section-title{margin-top:44px;color:var(--blue)}
.approved .lede{color:var(--muted);margin-top:20px}
.tile-grid{position:absolute;top:220px;left:172px;width:840px;display:grid;grid-template-columns:repeat(3,1fr);gap:8px}
.tile{position:relative;height:262px;overflow:hidden}
.tile::after{content:"";position:absolute;inset:0;background:linear-gradient(transparent 50%,rgba(0,0,0,.55))}
.tile-cap{position:absolute;z-index:1;left:16px;bottom:34px;color:var(--white);font-weight:600;font-size:14px}
.tile-sub{position:absolute;z-index:1;left:16px;bottom:16px;color:rgba(255,255,255,.8);font-size:10px}
.t1{background:linear-gradient(150deg,#c9d3dc,#7d8b98)}
.t2{background:linear-gradient(150deg,#8b96a2,#45505c)}
.t3{background:linear-gradient(150deg,#6b5a4c,#3a322b)}
.t4{background:linear-gradient(150deg,#8e8478,#4b463f)}
.t5{background:linear-gradient(150deg,#9aa4ad,#5c636a)}
.t6{background:linear-gradient(150deg,#d9a3a3,#a4484e)}

/* call band */
.call-band{top:1352px;height:160px}
.call-band .photo{background:linear-gradient(90deg,#6b4a2e,#2d2a2c 50%,#7a4f2b)}
.call-band .shade{background:rgba(20,22,26,.45)}
.call-band .btn-row{position:absolute;z-index:1;top:57px;left:0;width:1200px}

/* before after */
.compare{top:1512px;height:740px}
.compare-title{position:absolute;left:172px;top:62px;font-size:18px;font-weight:600;color:var(--blue-dark)}
.compare-frame{position:absolute;left:172px;top:116px;width:856px;height:568px}
.compare-top{position:absolute;left:0;top:0;width:856px;height:284px;background:linear-gradient(180deg,#b9c3cc,#e8eaec 60%,#9aa19c)}
.compare-bottom{position:absolute;left:0;top:284px;width:856px;height:284px;background:linear-gradient(180deg,#3b3c3e,#232427)}
.compare-handle{position:absolute;left:428px;top:284px;width:34px;height:34px;margin:-17px 0 0 -17px;border-radius:50%;border:2px solid var(--white);background:rgba(0,0,0,.35)}

/* stats */
.stats{top:2264px;height:540px;color:var(--white);text-align:center}
.stats .photo{background:linear-gradient(170deg,#525a61,#2a3036 60%,#41474b)}
.stats .shade{background:rgba(12,16,22,.75)}
.stats .eyebrow{padding-top:118px}
.stats .section-title{margin-top:8px;color:var(--blue)}
.stats .section-title .accent{color:var(--white)}
.stats .lede{margin-top:16px;color:rgba(255,255,255,.8)}
.stat-row{display:flex;justify-content:center;gap:120px;margin:30px 0 28px}
.stat b{display:block;font-size:30px;font-weight:700;line-height:1.1}
.stat span{font-size:11px}

/* video */
.video{top:2832px;height:410px;color:var(--white);text-align:center}
.video .photo{background:linear-gradient(180deg,#c9d0d6,#f1f2f2 55%,#8e948f)}
.video .shade{background:rgba(20,26,34,.35)}
.video-title{position:absolute;z-index:1;top:120px;left:0;width:1200px;font-size:30px;font-weight:600;color:var(--blue)}
.play{position:absolute;z-index:1;left:582px;top:204px;width:36px;height:36px;border-radius:50%;background:var(--blue-dark);display:flex;align-items:center;justify-content:center}

/* news */
.news{top:3288px;height:576px;background:var(--light);text-align:center}
.news .eyebrow{margin-top:64px;color:var(--muted)}
.news .section-title{margin-top:10px}
.card-row{position:absolute;top:176px;left:228px;width:744px;display:flex;gap:28px}
.card{width:229px;text-align:left;background:var(--white)}
.card-img{height:220px;background:radial-gradient(circle at 50% 50%,#e8ddd0 0,#c97d5a 30%,#b13a3a 60%,#5e2a50 100%)}
.card-body{padding:14px 14px 18px;border-left:3px solid var(--blue);margin:10px 0 0 12px}
.card-body h3{font-size:12px;font-weight:600;color:var(--blue-dark)}
.card-body p{font-size:10px;color:var(--muted);margin-top:6px}
.arrow{position:absolute;z-index:1;top:290px;width:24px;height:24px}

/* quote */
.quote{top:3888px;height:524px;color:var(--white);text-align:center}
.quote .photo{background:linear-gradient(170deg,#5e656b,#2e343a 55%,#4a4f52)}
.quote .shade{background:rgba(10,13,18,.72)}
.quote .eyebrow{padding-top:92px}
.quote .section-title{margin-top:14px;font-size:30px;line-height:1.3}
.quote .lede{color:rgba(255,255,255,.8)}
.quote .btn-row{margin-top:34px}

/* partners */
.partners{top:4412px;height:168px;background:var(--blue-band);color:var(--white)}
.partner-row{position:absolute;top:0;left:110px;width:980px;height:168px;display:flex;align-items:center;justify-content:space-between}
.partner{font-size:22px;font-weight:600;display:flex;align-items:center;gap:10px}
.partner i{width:16px;height:16px;background:var(--white);display:block}
.partners .arrow{top:72px}

/* footer */
.site-footer{top:4580px;height:380px;background:var(--night);color:var(--white)}
.footer-photo{position:absolute;right:0;top:0;width:440px;height:380px;background:linear-gradient(90deg,#0d1014,#6d7277 45%,#b8bdbf)}
.footer-col{position:absolute;top:54px;width:280px}
.footer-col h4{font-size:14px;font-weight:600;margin-bottom:16px}
.footer-col p{font-size:11px;line-height:1.7;color:rgba(255,255,255,.7)}
.footer-col .link{color:var(--blue);font-size:13px;margin-top:6px}
.footer-col .btn{height:40px;font-size:12px;margin-top:28px}
</style>
</head>
<body>

<section class="hero">
  <div class="photo" role="img" aria-label="Photo of a tiled roof with storm vent under grey skies"></div>
  <div class="shade"></div>
  <header class="site-header">
    <div class="brand"><span class="brand-dot"></span>GALE SENTRY</div>
    <nav class="main-nav">
      <a href="#">Home</a><a href="#">About Us</a><a href="#">Residential</a><a href="#">Commercial</a><a href="#">Contact</a>
      <span class="nav-phone"><svg viewBox="0 0 24 24" fill="#fff"><path d="M6.6 10.8a15 15 0 006.6 6.6l2.2-2.2a1 1 0 011-.25 11.4 11.4 0 003.6.57 1 1 0 011 1V20a1 1 0 01-1 1A17 17 0 013 4a1 1 0 011-1h3.5a1 1 0 011 1c0 1.25.2 2.45.57 3.57a1 1 0 01-.25 1z"/></svg>555 318-4072</span>
    </nav>
  </header>
  <div class="hero-copy">
    <p class="hero-kicker">We Know You</p>
    <h1 class="hero-title">Get protected for all the storms ahead!<br>Get the Gale Sentry!</h1>
    <div class="btn-row">
      <a class="btn" href="#">Call Now: 555 318-4072</a>
      <a class="btn" href="#">Start Your Free Quote <svg viewBox="0 0 12 12"><path d="M2 6h8M7 3l3 3-3 3" stroke="#fff" stroke-width="1.6" fill="none"/></svg></a>
    </div>
  </div>
</section>

<section class="approved">
  <h2 class="section-title">Roofing Vents <span class="accent">Approved</span></h2>
  <p class="lede">Lorem ipsum dolor sit amet, consectetur adipiscing elit. Donec porttitor tempus ipsum. Praesent mattis libero quis cursus, sed tincidunt ex orci posuere pretium. Vivamus lacus diam, vel dapibus nec dolor laoreet.</p>
  <div class="tile-grid">
    <div class="tile t1" role="img" aria-label="Steel roof framing under construction"><span class="tile-cap">Proven hurricane protection</span><span class="tile-sub">Lorem ipsum dolor sit</span></div>
    <div class="tile t2" role="img" aria-label="Metal roof structure from below"><span class="tile-cap">Proven hurricane protection</span><span class="tile-sub">Lorem ipsum dolor sit</span></div>
    <div class="tile t3" role="img" aria-label="Roofer installing shingles"><span class="tile-cap">Proven hurricane protection</span><span class="tile-sub">Lorem ipsum dolor sit</span></div>
    <div class="tile t4" role="img" aria-label="Workers on a damaged rooftop"><span class="tile-cap">Proven hurricane protection</span><span class="tile-sub">Lorem ipsum dolor sit</span></div>
    <div class="tile t5" role="img" aria-label="Turbine roof vent close-up"><span class="tile-cap">Proven hurricane protection</span><span class="tile-sub">Lorem ipsum dolor sit</span></div>
    <div class="tile t6" role="img" aria-label="Red tile roof detail"><span class="tile-cap">Proven hurricane protection</span><span class="tile-sub">Lorem ipsum dolor sit</span></div>
  </div>
</section>

<section class="call-band">
  <div class="photo" role="img" aria-label="Wooden roof trusses against the sky"></div>
  <div class="shade"></div>
  <div class="btn-row">
    <a class="btn" href="#">Call Now: 555 318-4072</a>
    <a class="btn" href="#">Start Your Free Quote <svg viewBox="0 0 12 12"><path d="M2 6h8M7 3l3 3-3 3" stroke="#fff" stroke-width="1.6" fill="none"/></svg></a>
  </div>
</section>

<section class="compare">
  <h2 class="compare-title">See The <span class="accent">before &amp; after</span></h2>
  <div class="compare-frame">
    <div class="compare-top" role="img" aria-label="White colonial building facade after restoration"></div>
    <div class="compare-bottom" role="img" aria-label="Dark damaged building facade before restoration"></div>
    <div class="compare-handle"></div>
  </div>
</section>

<section class="stats">
  <div class="photo" role="img" aria-label="Aerial view of a storm-hit neighbourhood"></div>
  <div class="shade"></div>
  <div class="inner">
    <p class="eyebrow">We Know You</p>
    <h2 class="section-title">Construction Vehicle <span class="accent">Protection</span></h2>
    <p class="lede">Lorem ipsum dolor sit amet, consectetur adipiscing elit. Donec porttitor tempus ipsum. Praesent mattis libero quis cursus, sed tincidunt ex orci posuere pretium. Vivamus lacus diam.</p>
    <div class="stat-row">
      <div class="stat"><b>300</b><span>MPH Tested</span></div>
      <div class="stat"><b>1,999</b><span>MPH Tested</span></div>
      <div class="stat"><b>96%</b><span>MPH Tested</span></div>
    </div>
    <div class="btn-row">
      <a class="btn" href="#">Call Now: 555 318-4072</a>
      <a class="btn" href="#">Start Your Free Quote <svg viewBox="0 0 12 12"><path d="M2 6h8M7 3l3 3-3 3" stroke="#fff" stroke-width="1.6" fill="none"/></svg></a>
    </div>
  </div>
</section>

<section class="video">
  <div class="photo" role="img" aria-label="Video still of a white colonial building"></div>
  <div class="shade"></div>
  <h2 class="video-title">Reliable weather-proof protection since 1998</h2>
  <div class="play"><svg width="12" height="12" viewBox="0 0 12 12"><path d="M3 1l8 5-8 5z" fill="#fff"/></svg></div>
</section>

<section class="news">
  <p class="eyebrow">Latest News</p>
  <h2 class="section-title">Keep Up To Date With The <span class="accent">latest news</span></h2>
  <svg class="arrow" style="left:172px" viewBox="0 0 24 24"><path d="M15 5l-7 7 7 7" stroke="#7a8591" stroke-width="2" fill="none"/></svg>
  <div class="card-row">
    <article class="card"><div class="card-img" role="img" aria-label="Satellite image of a hurricane"></div><div class="card-body"><h3>Construction Hurricane Season</h3><p>January 12, 2019</p></div></article>
    <article class="card"><div class="card-img" role="img" aria-label="Satellite image of a hurricane"></div><div class="card-body"><h3>Construction Hurricane</h3><p>January 12, 2019</p></div></article>
    <article class="card"><div class="card-img" role="img" aria-label="Satellite image of a hurricane"></div><div class="card-body"><h3>Construction Hurricane Set</h3><p>January 12, 2019</p></div></article>
  </div>
  <svg class="arrow" style="left:1004px" viewBox="0 0 24 24"><path d="M9 5l7 7-7 7" stroke="#7a8591" stroke-width="2" fill="none"/></svg>
</section>

<section class="quote">
  <div class="photo" role="img" aria-label="Aerial view of storm-damaged houses"></div>
  <div class="shade"></div>
  <div class="inner">
    <p class="eyebrow">We Know You</p>
    <h2 class="section-title">Request a free,<br>no obligation quote</h2>
    <div class="divider"></div>
    <p class="lede">Lorem ipsum dolor sit amet, consectetur adipiscing elit. Donec porttitor tempus ipsum. Praesent mattis libero quis cursus, sed tincidunt ex orci posuere pretium. Vivamus lacus diam.</p>
    <div class="btn-row">
      <a class="btn" href="#">Call Now: 555 318-4072</a>
      <a class="btn" href="#">Start Your Free Quote <svg viewBox="0 0 12 12"><path d="M2 6h8M7 3l3 3-3 3" stroke="#fff" stroke-width="1.6" fill="none"/></svg></a>
    </div>
  </div>
</section>

<section class="partners">
  <svg class="arrow" style="left:20px" viewBox="0 0 24 24"><path d="M15 5l-7 7 7 7" stroke="#fff" stroke-width="2" fill="none"/></svg>
  <div class="partner-row">
    <span class="partner"><i></i>Verano Atelier</span>
    <span class="partner">Crumb &amp; Co.</span>
    <span class="partner">Harbor Stay Inn</span>
    <span class="partner">Coastal Parcel</span>
    <span class="partner">Bayside Sharks</span>
  </div>
  <svg class="arrow" style="left:1156px" viewBox="0 0 24 24"><path d="M9 5l7 7-7 7" stroke="#fff" stroke-width="2" fill="none"/></svg>
</section>

<footer class="site-footer">
  <div class="footer-photo" role="img" aria-label="White colonial building with palm trees"></div>
  <div class="footer-col" style="left:172px">
    <h4>Contact Us</h4>
    <p>Lorem ipsum dolor sit amet, consectetur adipiscing elit.</p>
    <p class="link">trevor@galesentry-demo.com</p>
    <p class="link">555 318-4072</p>
    <a class="btn" href="#">Send a Message <svg viewBox="0 0 12 12"><path d="M2 6h8M7 3l3 3-3 3" stroke="#fff" stroke-width="1.6" fill="none"/></svg></a>
  </div>
  <div class="footer-col" style="left:500px">
    <h4>Headquarters</h4>
    <p>Lorem ipsum dolor sit amet, consectetur adipiscing elit. Sed do eiusmod tempor.</p>
    <p class="link">555-0199-782</p>
  </div>
</footer>

</body>
</html>
```